New webpage design for Varplen.se, participant management system informationpage.

Project Brief: New Website Design for Varplen.se (Participant Management System)
About Varplen.se:
Varplen.se is an established participant management system used by organizations and course providers in Sweden to handle event and course registrations. Our website’s primary audience is course providers, event organizers, and potential users seeking efficient management tools.
Project Goal:
We are launching a new public-facing website for Varplen.se, which will present information about our system, features, FAQ, pricing, news, testimonials, and more. The new site will be built in Umbraco CMS and should follow our visual identity as described in the attached graphic manual.
Deliverables:
We need complete, modern, and responsive page designs (desktop and mobile) for the following pages:
- Home page (landing page)
- Features page
- FAQ page
- About Us page
- Contact Us / Book a Demo page
- Pricing page
- Testimonials page
- News / Blog page
Design Guidelines:
- Please use the attached Lumoxa graphic manual for guidance (Lumoxa is a sister project; use the same branding).
- The Varplen.se logo is attached and must be included.
- Please use the blue color palette variant from the guide.
- Typography and graphic elements should be consistent with the manual.
- Designs must be suitable for implementation in Umbraco CMS (avoid overly complex layouts or animations that might be difficult to develop).
- All designs should be responsive and work well on desktop, tablet, and mobile.
- Final deliverables should be provided in Figma or Adobe XD (preferably Figma).
What We Like:
- Clean, modern, Scandinavian style.
- Clear navigation and strong hierarchy.
- Readable, accessible layouts.
What to Avoid:
- Overly playful or cartoonish elements.
- Too much clutter or excessive graphical elements.
- Dark color schemes (please focus on blue/light).
References:
- Our current site: https://varplen-example.se
- Graphic manual (see attachment)
- Varplen logo (see attachment)
Additional Notes:
- The new design should improve clarity, usability, and visual appeal compared to our current site.
- Feel free to suggest visual improvements, but remain consistent with our brand guidelines.
Other font styles liked:
- Orev and Cabin. See attached font files

```html
<!DOCTYPE html>
<html lang="en">
<head>
<meta charset="utf-8">
<title>Varplen.se – Participant Management</title>
<link href="https://fonts.googleapis.com/css2?family=Cabin:wght@400;500;600;700&family=Saira:wght@500;600;700&display=swap" rel="stylesheet">
<style>
:root{
  --blue:#2ba4e6;
  --blue-dark:#1279c4;
  --navy:#1c2330;
  --navy-2:#262e3c;
  --ink:#1d1f24;
  --muted:#6b7280;
  --light:#f3f5f8;
  --white:#ffffff;
  --star:#f5a623;
}
*{box-sizing:border-box;margin:0;padding:0}
html,body{width:1200px;height:3992px;overflow:hidden}
body{font-family:'Cabin',sans-serif;color:var(--ink);background:var(--white);position:relative}
section,header,footer{position:absolute;left:0;width:1200px}
.btn{display:inline-block;border-radius:24px;font-size:15px;font-weight:600;padding:12px 26px}
.btn-blue{background:var(--blue);color:var(--white)}
.btn-white{background:var(--white);color:var(--blue)}
.eyebrow{color:var(--blue);font-size:16px;font-weight:600;text-align:center}
.title{font-family:'Saira',sans-serif;font-weight:600;font-size:48px;text-align:center;line-height:1.1}
.intro{font-size:16px;color:var(--muted);text-align:center;line-height:1.6;width:760px;margin:14px auto 0}

/* hero */
.hero{top:0;height:600px;background:linear-gradient(90deg,#1a2230 0%,#2b3340 45%,#5d6670 100%);overflow:hidden}
.hero-photo{position:absolute;right:0;top:0;width:680px;height:560px;background:linear-gradient(110deg,rgba(40,48,60,0) 0%,#6b747c 40%,#9aa1a6 70%,#4d565f 100%)}
.nav{position:absolute;top:20px;left:100px;right:100px;height:60px;display:flex;align-items:center;justify-content:space-between}
.logo{font-family:'Cabin',sans-serif;font-weight:600;font-size:52px;color:var(--white);letter-spacing:1px}
.menu{display:flex;gap:38px;color:var(--white);font-size:15px;margin-top:34px}
.nav .btn{position:absolute;right:0;top:0;padding:10px 22px;font-size:14px}
.hero h1{position:absolute;left:100px;top:160px;font-family:'Saira',sans-serif;font-weight:600;font-size:50px;color:var(--white);line-height:1.12}
.hero p{position:absolute;left:100px;top:290px;width:480px;font-size:22px;color:var(--white);line-height:1.35}
.hero .cta{position:absolute;left:100px;top:412px;display:flex;gap:18px}
.hero-wave{position:absolute;left:0;bottom:0}

/* heritage */
.heritage{top:600px;height:640px}
.heritage .title{margin-top:40px}
.heritage .eyebrow{margin-top:14px}
.heritage-photo{position:absolute;left:160px;top:140px;width:290px;height:290px;border-radius:50%;background:radial-gradient(circle at 40% 40%,#d9d2c9,#8e8a86 70%,#555 100%);border:8px solid var(--white);box-shadow:0 0 0 3px var(--blue)}
.heritage-text{position:absolute;left:610px;top:160px;width:480px;font-size:17px;line-height:1.6;color:#3b3f46}
.heritage-text p+p{margin-top:18px;color:var(--muted);font-size:15px}
.heritage-text .btn{margin-top:22px}

/* capabilities */
.capabilities{top:1240px;height:580px;background:linear-gradient(180deg,#2a9ddf,#1c86cc)}
.capabilities .eyebrow{color:var(--white);margin-top:50px}
.capabilities .title{color:var(--white);margin-top:4px}
.cards{position:absolute;top:168px;left:132px;display:flex;gap:32px}
.card{width:292px;height:340px;background:var(--white);border-radius:20px;padding:40px 32px;box-shadow:0 10px 30px rgba(0,0,0,.15)}
.card:last-child{width:316px}
.icon{width:52px;height:52px;border-radius:50%;background:#eaf5fc;display:flex;align-items:center;justify-content:center}
.card h3{font-size:20px;margin-top:26px;font-weight:700}
.card p{font-size:14px;color:var(--muted);line-height:1.6;margin-top:12px}

/* testimonials */
.testimonials{top:1820px;height:580px}
.testimonials .eyebrow{margin-top:64px}
.testimonials .title{margin-top:2px}
.quotes{position:absolute;top:240px;left:120px;display:flex;gap:48px}
.quote{width:472px;height:260px;border-radius:20px;padding:34px 44px;box-shadow:0 8px 28px rgba(0,0,0,.1);background:var(--white)}
.quote-mark{font-family:'Saira',sans-serif;color:var(--blue);font-size:80px;line-height:.8;font-weight:700}
.quote p{font-size:15px;color:var(--muted);line-height:1.6;margin-top:14px}
.stars{color:var(--star);font-size:16px;margin-top:18px;letter-spacing:2px}
.quote h4{font-size:15px;font-weight:700;letter-spacing:.5px;margin-top:4px}
.arrows{position:absolute;right:44px;top:358px;display:flex;flex-direction:column;gap:16px}

/* faq */
.faq{top:2400px;height:640px;background:var(--light)}
.faq .eyebrow{margin-top:56px}
.faq .title{margin-top:2px}
.faq-list{position:absolute;top:232px;left:240px;width:720px;display:flex;flex-direction:column;gap:26px}
.faq-item{height:56px;background:var(--white);border-radius:28px;box-shadow:0 4px 14px rgba(0,0,0,.08);display:flex;align-items:center;padding:0 26px;font-size:16px}
.faq-item span{width:40px;font-weight:600}
.faq-item em{font-style:normal;flex:1}
.plus{width:20px;height:20px;border-radius:50%;background:var(--ink);color:var(--white);font-size:16px;display:flex;align-items:center;justify-content:center;line-height:1}

/* why */
.why{top:3040px;height:500px;background:linear-gradient(180deg,#2ba4e6,#57b8ec 60%,#2a9ddf);overflow:hidden}
.why .eyebrow{color:var(--white);margin-top:64px}
.why .title{color:var(--white);margin-top:2px}
.why .intro{color:var(--white)}
.steps{position:absolute;top:250px;left:80px;width:1040px;display:flex;justify-content:space-between}
.steps-line{position:absolute;top:290px;left:160px;width:880px;border-top:2px dashed rgba(255,255,255,.7)}
.step{width:260px;text-align:center;color:var(--ink);font-size:17px;line-height:1.3;position:relative}
.step-icon{width:80px;height:80px;border-radius:50%;background:var(--white);margin:0 auto 22px;display:flex;align-items:center;justify-content:center;box-shadow:0 6px 18px rgba(0,0,0,.15)}
.step-icon.dark{background:var(--navy)}

/* footer */
.footer{top:3500px;height:492px;background:var(--navy)}
.footer-wave{position:absolute;top:-2px;left:0}
.footer .logo{position:absolute;left:110px;top:100px;font-size:60px}
.cols{position:absolute;top:90px;left:450px;display:flex;gap:100px;color:var(--white)}
.col h5{font-size:16px;font-weight:700;letter-spacing:.5px;margin-bottom:12px}
.col li{list-style:none;font-size:14px;line-height:1.75}
.col li::before{content:"›";color:var(--blue);margin-right:10px}
.col p{font-size:14px;line-height:1.4;width:240px}
.subscribe{margin-top:14px;width:240px;height:34px;background:var(--white);border-radius:17px;display:flex;align-items:center;justify-content:space-between;padding:0 4px 0 14px;font-size:12px;color:var(--muted)}
.subscribe b{background:var(--blue);color:var(--white);border-radius:14px;padding:6px 14px;font-size:12px}
.contact{position:absolute;top:366px;left:110px;right:110px;display:flex;justify-content:space-between;color:var(--white);font-size:14px;border-top:1px solid rgba(255,255,255,.15);padding-top:20px}
.contact div{display:flex;align-items:center;gap:12px}
.dot{width:30px;height:30px;border-radius:50%;background:var(--blue);display:flex;align-items:center;justify-content:center}
.copy-bar{position:absolute;top:440px;left:0;width:100%;height:52px;background:var(--navy-2)}
.copy{position:absolute;top:456px;width:100%;text-align:center;color:var(--white);font-size:14px;letter-spacing:1px}
</style>
</head>
<body>

<header class="hero">
  <div class="hero-photo" role="img" aria-label="Photo of colleagues in a bright office discussing work at a laptop"></div>
  <nav class="nav">
    <div class="logo">varplen.</div>
    <div class="menu"><span>Home</span><span>Features</span><span>About Us</span><span>Pricing</span><span>Reviews</span><span>News</span><span>Faqs</span></div>
    <span class="btn btn-blue">Book a Demo</span>
  </nav>
  <h1>Smart Registration for<br>Courses and Events</h1>
  <p>Varplen.se simplifies participant management so you can focus on delivering great experiences.</p>
  <div class="cta"><span class="btn btn-blue">Book a Demo</span><span class="btn btn-white">Explore Features</span></div>
  <svg class="hero-wave" width="1200" height="110" viewBox="0 0 1200 110" preserveAspectRatio="none">
    <path d="M0 110 L0 80 Q300 20 600 0 Q900 20 1200 80 L1200 110Z" fill="#2ba4e6"/>
    <path d="M0 110 L0 96 Q300 44 600 24 Q900 44 1200 96 L1200 110Z" fill="#ffffff"/>
  </svg>
</header>

<section class="heritage">
  <h2 class="title">Our Heritage &amp; Vision</h2>
  <div class="eyebrow">Years Of Beautiful Results</div>
  <div class="heritage-photo" role="img" aria-label="Photo of two women working together at a laptop"></div>
  <div class="heritage-text">
    <p>Varplen.se is an established participant management system used by organizations and course providers in Sweden to handle event and course registrations. Our website's primary audience is course providers, event organizers, and potential users seeking efficient management tools.</p>
    <p>Every registration, payment and confirmation is handled in one place, so your team spends less time on admin and more time on the people attending your courses and events.</p>
    <span class="btn btn-blue">Explore More</span>
  </div>
</section>

<section class="capabilities">
  <div class="eyebrow">Features</div>
  <h2 class="title">Our Key Capabilities</h2>
  <div class="cards">
    <div class="card">
      <div class="icon"><svg width="26" height="26" viewBox="0 0 24 24" fill="none" stroke="#1d1f24" stroke-width="1.8"><rect x="5" y="3" width="14" height="18" rx="2"/><path d="M8 8h8M8 12h8M8 16h5"/></svg></div>
      <h3>Flexible Forms</h3>
      <p>Build registration forms that match each course, with custom fields, limits and options that adapt as your needs grow.</p>
    </div>
    <div class="card">
      <div class="icon"><svg width="26" height="26" viewBox="0 0 24 24" fill="none" stroke="#1d1f24" stroke-width="1.8"><rect x="7" y="2" width="10" height="20" rx="2"/><path d="M11 18h2"/></svg></div>
      <h3>Mobile Friendly</h3>
      <p>Participants sign up from any phone or tablet, and organizers can follow bookings and check in guests on the go.</p>
    </div>
    <div class="card">
      <div class="icon"><svg width="26" height="26" viewBox="0 0 24 24" fill="none" stroke="#1d1f24" stroke-width="1.8"><path d="M12 2l8 3v6c0 5-3.5 9-8 11-4.5-2-8-6-8-11V5z"/><path d="M8.5 12l2.5 2.5 4.5-5"/></svg></div>
      <h3>Secure Data Handling</h3>
      <p>Personal data is stored safely in line with GDPR, with clear access control for everyone on your team.</p>
    </div>
  </div>
</section>

<section class="testimonials">
  <div class="eyebrow">What Our Users Say</div>
  <h2 class="title">Our Happy Customers</h2>
  <p class="intro">Course providers across Sweden rely on our system every day. Here is what a few of them say about running their registrations with us.</p>
  <div class="quotes">
    <div class="quote">
      <div class="quote-mark">“</div>
      <p>Setting up our spring courses took minutes instead of days. Payments and confirmations now run on their own, and our participants love how simple it is.</p>
      <div class="stars">★★★★★</div>
      <h4>MAJA LINDQVIST</h4>
    </div>
    <div class="quote">
      <div class="quote-mark">“</div>
      <p>We finally have one clear overview of every event. Reports are easy to export and support always answers quickly when we need help.</p>
      <div class="stars">★★★★★</div>
      <h4>MAJA LINDQVIST</h4>
    </div>
  </div>
  <div class="arrows">
    <svg width="20" height="20" viewBox="0 0 20 20" fill="none" stroke="#1d1f24" stroke-width="2"><path d="M15 10H5M9 6l-4 4 4 4"/></svg>
    <svg width="20" height="20" viewBox="0 0 20 20" fill="none" stroke="#1d1f24" stroke-width="2"><path d="M5 10h10M11 6l4 4-4 4"/></svg>
  </div>
</section>

<section class="faq">
  <div class="eyebrow">Frequently Asked Questions</div>
  <h2 class="title">Common Questions</h2>
  <p class="intro">Find quick answers about setup, pricing and daily use. If your question is not listed here, our team is happy to help you out.</p>
  <div class="faq-list">
    <div class="faq-item"><span>(01)</span><em>How quickly can we start taking registrations?</em><b class="plus">+</b></div>
    <div class="faq-item"><span>(02)</span><em>Which payment methods can participants use?</em><b class="plus">+</b></div>
    <div class="faq-item"><span>(03)</span><em>Can we customise forms for each course?</em><b class="plus">+</b></div>
    <div class="faq-item"><span>(04)</span><em>How is participant data kept secure?</em><b class="plus">+</b></div>
    <div class="faq-item"><span>(05)</span><em>Do you offer support during onboarding?</em><b class="plus">+</b></div>
  </div>
</section>

<section class="why">
  <div class="eyebrow">Join With Us</div>
  <h2 class="title">Why Choose Us</h2>
  <p class="intro">From the first sign-up to the final report, we make every step of participant management simple, reliable and quick.</p>
  <div class="steps-line"></div>
  <div class="steps">
    <div class="step"><div class="step-icon"><svg width="34" height="34" viewBox="0 0 24 24" fill="none" stroke="#1d1f24" stroke-width="1.6"><rect x="5" y="3" width="14" height="18" rx="2"/><path d="M9 12l2 2 4-4"/></svg></div>Easy Registration Setup</div>
    <div class="step"><div class="step-icon dark"><svg width="34" height="34" viewBox="0 0 24 24" fill="none" stroke="#ffffff" stroke-width="1.6"><circle cx="12" cy="12" r="8"/><path d="M8.5 12l2.5 2.5 4.5-5"/></svg></div>Automated Confirmations<br>&amp; Reminders</div>
    <div class="step"><div class="step-icon"><svg width="34" height="34" viewBox="0 0 24 24" fill="none" stroke="#1d1f24" stroke-width="1.6"><rect x="3" y="6" width="18" height="12" rx="2"/><path d="M3 10h18M7 15h4"/></svg></div>Integrated Payments</div>
    <div class="step"><div class="step-icon"><svg width="34" height="34" viewBox="0 0 24 24" fill="none" stroke="#1d1f24" stroke-width="1.6"><rect x="3" y="4" width="18" height="13" rx="2"/><path d="M8 21h8M12 17v4M7 13l3-3 3 2 4-4"/></svg></div>Real-Time Participant<br>Overview</div>
  </div>
</section>

<footer class="footer">
  <svg class="footer-wave" width="1200" height="56" viewBox="0 0 1200 56" preserveAspectRatio="none">
    <path d="M0 0 H1200 V20 Q900 56 600 56 Q300 56 0 20Z" fill="#2ba4e6"/>
    <path d="M0 0 H1200 V6 Q900 38 600 40 Q300 38 0 6Z" fill="#57b8ec"/>
  </svg>
  <div class="logo">varplen.</div>
  <div class="cols">
    <div class="col"><h5>QUICK LINKS</h5><ul><li>Home</li><li>About Us</li><li>Features</li><li>Testimonials</li><li>FAQ'S</li><li>Contact Us</li></ul></div>
    <div class="col"><h5>RENTING</h5><ul><li>Pricing</li><li>Book a Demo</li><li>News</li><li>Blogs</li></ul></div>
    <div class="col"><h5>STAY POWERED. STAY<br>INFORMED</h5><p>Be the First to Know. Sign Up for New Listing</p><div class="subscribe">Enter Address <b>Send</b></div></div>
  </div>
  <div class="contact">
    <div><span class="dot"><svg width="14" height="14" viewBox="0 0 24 24" fill="#fff"><path d="M12 2a7 7 0 0 0-7 7c0 5 7 13 7 13s7-8 7-13a7 7 0 0 0-7-7zm0 9.5a2.5 2.5 0 1 1 0-5 2.5 2.5 0 0 1 0 5z"/></svg></span>14 Fjordgatan, Suite 2, Uppsala 753 20, Sweden</div>
    <div><span class="dot"><svg width="14" height="14" viewBox="0 0 24 24" fill="#fff"><path d="M6.6 10.8a15 15 0 0 0 6.6 6.6l2.2-2.2a1 1 0 0 1 1-.25 11.4 11.4 0 0 0 3.6.57 1 1 0 0 1 1 1V20a1 1 0 0 1-1 1A17 17 0 0 1 3 4a1 1 0 0 1 1-1h3.5a1 1 0 0 1 1 1c0 1.25.2 2.45.57 3.57a1 1 0 0 1-.25 1z"/></svg></span>+46 10 555 0142</div>
    <div><span class="dot"><svg width="14" height="14" viewBox="0 0 24 24" fill="none" stroke="#fff" stroke-width="2"><rect x="3" y="5" width="18" height="14" rx="2"/><path d="M3 7l9 6 9-6"/></svg></span>info@varplen-example.se</div>
  </div>
  <div class="copy-bar"></div>
  <div class="copy">(C) COPYRIGHT | ALL RIGHTS RESERVED</div>
</footer>

</body>
</html>
```